Business Card Design Project

I am a Homoeopath and would like a new business card which represents my clinic and how I work...My clinic Thistle Wellness is situated near Calderwood forest, you can hear the lyrebirds calling all the time!
My work is holistic and deals with shifting energy in order to create balance within the body. There is a very strong spiritual element to my work.
I have uploaded my current card, As far as the actual details on the front and the back I would like these to remain in the same structure...

Target Market(s)

those looking for alternative health therapies... all of my patients are referred to me so I am not concerned about fitting into a mainstream box

Industry/Entity Type

Clinic

Requirements
Must have
• This card must not look corporate!
be creative and different

Nice to have
• I am picturing a tree of life with roots heading into the earth and on it is a white peacock, maybe a body of water and a full moon nearby?

```html
<!DOCTYPE html>
<html lang="en">
<head>
<meta charset="utf-8">
<title>Thistle Wellness — Business Card</title>
<link href="https://fonts.googleapis.com/css2?family=Didact+Gothic&display=swap" rel="stylesheet">
<style>
  :root {
    --night: #0d1130;
    --deep: #05060f;
    --ink-white: #ffffff;
    --soft-grey: #c9cbd6;
    --emblem-dark: #0a0a12;
    --emblem-lilac: #b58bd6;
    --emblem-rose: #e08fb4;
  }
  * { margin: 0; padding: 0; box-sizing: border-box; }
  html, body {
    width: 685px; height: 1200px; overflow: hidden;
    background: var(--deep);
  }
  .card {
    position: relative;
    width: 685px; height: 1200px; overflow: hidden;
    font-family: "Didact Gothic", "Century Gothic", sans-serif;
    color: var(--ink-white);
  }
  .card__sky {
    position: absolute; inset: 0;
    background:
      radial-gradient(ellipse 360px 300px at 620px 430px, rgba(228,106,154,0.85), transparent 70%),
      radial-gradient(ellipse 300px 260px at 520px 600px, rgba(138,95,184,0.7), transparent 70%),
      radial-gradient(ellipse 380px 300px at 120px 760px, rgba(90,159,214,0.75), transparent 70%),
      radial-gradient(ellipse 260px 200px at 360px 820px, rgba(143,211,230,0.55), transparent 70%),
      radial-gradient(ellipse 420px 280px at 300px 140px, rgba(40,46,96,0.9), transparent 75%),
      linear-gradient(180deg, var(--night) 0%, #1c1f4a 45%, #263a6a 62%, var(--deep) 100%);
  }
  .emblem {
    position: absolute;
    left: 86px; top: 64px;
    width: 512px; height: 512px;
    border-radius: 50%;
    background:
      radial-gradient(circle at 62% 42%, var(--emblem-rose) 0%, var(--emblem-lilac) 28%, transparent 55%),
      linear-gradient(180deg, #2a2a36 0%, var(--emblem-dark) 100%);
  }
  .brand {
    position: absolute;
    left: 0; right: 0; top: 690px;
    text-align: center;
    font-size: 72px;
    font-weight: 400;
    line-height: 1;
    color: var(--ink-white);
  }
  .tagline {
    position: absolute;
    left: 0; right: 0; top: 832px;
    display: flex; justify-content: center; align-items: center; gap: 14px;
    font-size: 25px;
    line-height: 1;
    letter-spacing: 1px;
    text-transform: uppercase;
  }
  .tagline__rule { width: 26px; height: 2px; background: var(--ink-white); }
  .contact {
    position: absolute;
    left: 66px; top: 992px;
    line-height: 1;
  }
  .contact__name { font-size: 25px; letter-spacing: 0.5px; text-transform: uppercase; }
  .contact__credentials { margin-top: 10px; font-size: 22px; color: var(--soft-grey); opacity: 0.8; }
  .contact__email { margin-top: 22px; font-size: 25px; }
  .contact__phone { margin-top: 6px; font-size: 25px; }
</style>
</head>
<body>
  <main class="card">
    <div class="card__sky" role="img" aria-label="Starry nebula sky in navy, magenta and cyan tones"></div>
    <div class="emblem" role="img" aria-label="Round emblem area in dark and lilac tones"></div>
    <h1 class="brand">Thistle Wellness</h1>
    <p class="tagline"><span class="tagline__rule"></span>Classical Homoeopathy<span class="tagline__rule"></span></p>
    <section class="contact">
      <p class="contact__name">Maren Okafor</p>
      <p class="contact__credentials">Ad Dip Hom Med Memb AHA Aroh Regd</p>
      <p class="contact__email">maren.okafor@tealmail.com</p>
      <p class="contact__phone">0400-123-987</p>
    </section>
  </main>
</body>
</html>
```